Fox & Fern honey company needs a label design.

We need a label design for a new honey company, based in the state of Florida called 'Fox & Fern". We are supplying our online customers with the highest quality of the various kinds of raw honey. Our product is honey in the oval hexagon glass jar with black lid. We would like to see designs that use black background with gold font .
In the upper part of the label is gold flying Honey Bee (profile, silhouette). The name of the brand "Fox & Fern" - Caramel font. Additional fonts are Cinzel, Source Sans Pro. Label measurements 2.6" by 3".
Label content:
Fox & Fern
RAW HONEY
wildflower
PURE & NATURAL
made by Florida Bees
foxandfernhoney.com
NET WT 12oz (340g)

The final design should have eye catching, luxurious look.
Updates

Target Market(s)

Luxury

Industry/Entity Type

Food (bee products)

Other font styles liked:
• caramel

Colors

Designer to choose colors to be used in the design.

Requirements
Must have
• Gold letters on black background, Drawing of a bee, flying in profile

```html
<!DOCTYPE html>
<html lang="en">
<head>
<meta charset="utf-8">
<title>Fox &amp; Fern Raw Honey Label</title>
<link href="https://fonts.googleapis.com/css2?family=Caramel&family=Cinzel:wght@400&family=Source+Sans+3:wght@400;600&display=swap" rel="stylesheet">
<style>
  :root {
    --backdrop: #6e6e6e;
    --label-black: #000000;
    --gold: #e9c84f;
    --gold-light: #fdf0b0;
    --gold-deep: #c9a53a;
    --comb-olive: #4a3f1c;
    --band-text: #1a1a1a;
  }
  * { margin: 0; padding: 0; box-sizing: border-box; }
  html, body {
    width: 1200px;
    height: 849px;
    overflow: hidden;
  }
  body {
    background: var(--backdrop);
    position: relative;
  }
  .label {
    position: absolute;
    left: 304px;
    top: 83px;
    width: 592px;
    height: 683px;
    background: var(--label-black);
    overflow: hidden;
  }
  .honeycomb-field {
    position: absolute;
    left: 0; top: 0;
    width: 100%;
    height: 340px;
    background: linear-gradient(to bottom, rgba(74,63,28,0.75) 0%, rgba(74,63,28,0.35) 45%, rgba(0,0,0,0) 100%);
  }
  .bee-emblem {
    position: absolute;
    left: 189px;
    top: 34px;
    width: 213px;
    height: 137px;
    background: radial-gradient(ellipse at center, var(--gold-light) 0%, var(--gold) 40%, rgba(233,200,79,0) 72%);
  }
  .brand-row {
    position: absolute;
    left: 0; top: 254px;
    width: 100%;
    height: 60px;
  }
  .brand-rule {
    position: absolute;
    top: 28px;
    height: 2px;
    background: var(--gold);
  }
  .brand-rule--left { left: 60px; width: 109px; }
  .brand-rule--right { left: 425px; width: 97px; }
  .brand-name {
    position: absolute;
    left: 0; top: 0;
    width: 100%;
    text-align: center;
    font-family: 'Caramel', cursive;
    font-size: 52px;
    line-height: 60px;
    color: var(--gold);
  }
  .product-title {
    position: absolute;
    left: 0; top: 310px;
    width: 100%;
    text-align: center;
    font-family: 'Cinzel', serif;
    font-size: 64px;
    line-height: 86px;
    letter-spacing: 1px;
    color: var(--gold);
    background: linear-gradient(to bottom, var(--gold-deep), var(--gold-light) 55%, var(--gold));
    -webkit-background-clip: text;
    background-clip: text;
    -webkit-text-fill-color: transparent;
  }
  .title-rule {
    position: absolute;
    left: 181px;
    top: 402px;
    width: 229px;
    height: 2px;
    background: var(--gold);
  }
  .variety {
    position: absolute;
    left: 0; top: 444px;
    width: 100%;
    text-align: center;
    font-family: 'Caramel', cursive;
    font-size: 34px;
    line-height: 40px;
    color: var(--gold);
  }
  .tagline {
    position: absolute;
    left: 0; top: 494px;
    width: 100%;
    text-align: center;
    font-family: 'Cinzel', serif;
    font-size: 23px;
    line-height: 30px;
    letter-spacing: 5px;
    color: var(--gold);
  }
  .maker {
    position: absolute;
    left: 59px; top: 570px;
    font-family: 'Source Sans 3', sans-serif;
    font-size: 18px;
    line-height: 23px;
    letter-spacing: 1.5px;
    color: var(--gold);
  }
  .net-weight {
    position: absolute;
    right: 58px; top: 580px;
    font-family: 'Source Sans 3', sans-serif;
    font-weight: 600;
    font-size: 22px;
    line-height: 28px;
    color: var(--gold);
  }
  .web-band {
    position: absolute;
    left: 0; bottom: 0;
    width: 100%;
    height: 44px;
    background: linear-gradient(to right, var(--gold) 0%, var(--gold-light) 50%, var(--gold) 100%);
    text-align: center;
    font-family: 'Source Sans 3', sans-serif;
    font-size: 18px;
    line-height: 44px;
    color: var(--band-text);
  }
</style>
</head>
<body>
  <main class="label">
    <div class="honeycomb-field" role="img" aria-label="Gold honeycomb pattern fading into black"></div>
    <div class="bee-emblem" role="img" aria-label="Gold honey bee illustration with outspread wings"></div>

    <div class="brand-row">
      <span class="brand-rule brand-rule--left"></span>
      <h1 class="brand-name">Fox &amp; Fern</h1>
      <span class="brand-rule brand-rule--right"></span>
    </div>

    <h2 class="product-title">RAW HONEY</h2>
    <span class="title-rule"></span>

    <p class="variety">wildflower</p>
    <p class="tagline">PURE &amp; NATURAL</p>

    <p class="maker">made by<br>Florida Bees</p>
    <p class="net-weight">12oz (340g)</p>

    <footer class="web-band">foxandfernhoney.com</footer>
  </main>
</body>
</html>
```